Skincare Clinic specializing in treating difficult skin conditions needs a web design

We want to restructure and rehash our current webdesigns. The current ones are dated and look very old fashioned also, they are not structured well.

The current websites need to get an uplift in look and become more classy and modern with navigation ease by structuring the information into ease of access

The current web address is
www.brellowderm.com.au and
www.velmarash.com.au

We also have international Partner website which is good and we need to better than them. So this website will act as a guide to better the new site
www.tenquil-drsorvan.com

But the new site should be more inclined towards a Blue colour or Aqua marine blue orientation and it needs to be Scientific giving authenticity to the medical industry we operate in.

Attached is a webdesign framework and architecture we would want to adopt. It is a schematic diagram and you can creatively adopt based on what you want to propose.

The website needs to be coded and Should be coded in WordPress such that it helps with SEO activity and google adwords pickup.

We will need the necessary pictures and we could provide them or agree to by them from the designers source.

Target Market(s)

Patients with Skin Disease and people interested to book consultation or buy products for their Skin condition

Industry/Entity Type

Clinic

Coding

Coded - Design and coding required

Number of Pages Required

5+ page

Font styles to use
Other font styles liked:
• Use a light font denoting class.

Requirements
Must have
• Should be modern, Easy to navigate, mobile friendly and coded in wordpress
• Blue colour and should look scientific and medicinal
Nice to have
• Classy and creative
Should not have
• No Green colour or herbal look

```html
<!DOCTYPE html>
<html lang="en">
<head>
<meta charset="utf-8">
<title>Clearhaven – Dermal &amp; Skin Clinic</title>
<link rel="stylesheet" href="https://fonts.googleapis.com/css2?family=Jost:wght@300;400;500&family=Open+Sans:wght@400;600&family=Libre+Baskerville&display=swap">
<style>
:root{
  --blue:#0aa9ea;
  --blue-dark:#078fc6;
  --teal:#5cc6cf;
  --grey-btn:#bcbcbc;
  --book:#999;
  --ink:#3c3c3c;
  --muted:#8a8a8a;
  --line:#e2e2e2;
  --panel:#f7f7f7;
  --footer:#5b5b5b;
  --hero-a:#ffffff;
  --hero-b:#cfeef6;
}
*{box-sizing:border-box;margin:0;padding:0}
html,body{width:682px;height:1200px;overflow:hidden;background:#fff}
body{position:relative;font-family:"Open Sans",Arial,sans-serif;color:var(--ink)}
a{text-decoration:none}
.abs{position:absolute}
.sans-light{font-family:"Jost",Arial,sans-serif;font-weight:300}

/* header */
.promo{left:57px;top:22px;width:314px;height:71px;border:1px solid #999;background:linear-gradient(90deg,#f4f1ec,#fff 60%,#ece9e4)}
.promo-product{left:4px;top:3px;width:54px;height:63px;background:linear-gradient(180deg,#7a4a1e,#c58a3e);border-radius:2px}
.promo-product2{right:6px;top:16px;width:10px;height:50px;background:linear-gradient(180deg,#777,#222)}
.promo-title{left:70px;top:6px;font-family:"Libre Baskerville",Georgia,serif;font-size:12px;line-height:13px;color:#4a2a12}
.promo-btn{left:73px;top:43px;width:78px;height:20px;background:#fff;border:1px solid #ddd;border-radius:3px;font-size:8px;line-height:18px;text-align:center;color:#333}
.promo-price{left:190px;top:46px;width:102px;text-align:right;font-family:"Libre Baskerville",Georgia,serif;font-size:8px;line-height:9px;color:#4a2a12}
.promo-price small{font-size:7px}
.search{left:511px;top:23px;width:114px;height:18px;border:1px solid var(--line);font-size:7px;color:#ccc;padding:4px 7px}
.search svg{position:absolute;right:5px;top:3px}
.brand{left:452px;top:49px;display:flex;align-items:center;gap:8px}
.brand-name{font-family:"Jost",Arial,sans-serif;font-weight:500;color:var(--blue);font-size:22px;line-height:20px;text-align:right}
.brand-name span{display:block;font-size:11px;line-height:13px}
.brand-dot{width:30px;height:30px;border-radius:50%;background:var(--blue);display:block}

/* nav */
.nav{left:0;top:109px;width:682px;height:26px;background:var(--blue);display:flex;padding-left:57px}
.nav a{color:#fff;font-size:8px;line-height:26px;padding:0 13px;position:relative;letter-spacing:.2px}
.nav a+a::before{content:"";position:absolute;left:0;top:7px;height:12px;border-left:1px solid rgba(255,255,255,.6)}
.nav a.active{background:var(--blue-dark);padding:0 20px}

/* hero */
.hero{left:0;top:135px;width:682px;height:238px;background:linear-gradient(110deg,var(--hero-a) 30%,#e6f6fa 60%,var(--hero-b));border-bottom:1px solid var(--line)}
.hero-kicker{left:69px;top:40px;font-size:17px;color:#333}
.hero-title{left:68px;top:62px;font-size:33px;line-height:34px;color:#222;letter-spacing:.5px}
.hero-lede{left:69px;top:133px;width:330px;font-size:13.5px;line-height:20px;color:#333;font-family:"Jost",Arial,sans-serif;font-weight:300}
.btn{display:block;text-align:center;font-size:8px;color:#fff}
.btn-products{left:70px;top:180px;width:107px;height:27px;line-height:27px;background:var(--teal);color:#123;font-weight:600}
.btn-more{left:182px;top:180px;width:107px;height:27px;line-height:27px;background:var(--grey-btn)}
.hero-photo{left:404px;top:0;width:212px;height:238px;background:linear-gradient(180deg,rgba(230,205,190,.55),rgba(236,220,212,.35) 60%,rgba(220,238,244,0))}

/* service cards */
.card{top:405px;height:230px;border:1px solid var(--line);background:#fff}
.card-head{height:33px;background:#f4f4f4;border-bottom:1px solid var(--line);display:flex;align-items:center;padding-left:16px;gap:11px;font-family:"Jost",Arial,sans-serif;font-weight:300;font-size:15px;color:#333}
.card-head i{width:22px;height:22px;border-radius:50%;background:var(--blue);display:block}
.card-text{position:absolute;left:9px;width:160px;font-size:7.4px;line-height:11.5px;color:var(--muted)}
.field{position:absolute;left:9px;width:157px;height:25px;border:1px solid #eee;font-size:7px;color:#aaa;padding:7px 8px}
.card .photo{position:absolute;left:8px;top:41px;width:161px;height:95px}
.card-btn{position:absolute;left:8px;bottom:12px;width:159px;height:27px;line-height:27px;background:var(--blue);color:#fff;text-align:center;font-size:10.5px;font-family:"Jost",Arial,sans-serif;font-weight:400}
.book{background:var(--book);border:1px solid #888;bottom:13px;left:9px;width:158px;height:28px;line-height:26px}

/* about */
.about-band{left:0;top:680px;width:682px;height:262px;background:var(--panel);border-top:1px solid var(--line);border-bottom:1px solid var(--line)}
.eyebrow{font-family:"Jost",Arial,sans-serif;font-weight:300;color:var(--blue);font-size:12.5px}
.heading{font-family:"Jost",Arial,sans-serif;font-weight:300;color:#333;font-size:15px}
.doctor{left:60px;top:62px;width:130px;height:199px;background:linear-gradient(180deg,#f1f1f1 0%,#e4e9ef 30%,#d7dce3 70%,#cfd5dc)}
.about-copy{left:204px;width:190px;font-size:8px;line-height:12.5px;color:#333}
.bullets{left:204px;top:173px;width:190px;list-style:none;font-size:7px;line-height:12.5px;color:#333}
.bullets li::before{content:"›";color:#999;margin-right:5px}
.divider-v{left:401px;top:20px;height:230px;border-left:1px solid var(--line)}
.case{top:68px;width:99px;height:78px;border-radius:3px}
.arrows{left:598px;top:40px}
.viewall{font-size:8px;color:#333;font-weight:600}
.case-copy{left:417px;top:192px;width:212px;font-size:8px;line-height:12.5px;color:#333}

/* unique + testimonial */
.step{left:63px;width:23px;height:23px;border-radius:50%;color:#fff;font-size:11px;text-align:center;line-height:23px;font-family:"Jost",Arial,sans-serif}
.step-1{background:#2a9fe0}
.step-2{background:#48c3cc}
.step-text{left:94px;width:200px;font-size:8px;line-height:12.5px;color:#333}
.divider-h{left:64px;top:1049px;width:220px;border-top:1px solid #eee}
.brace{left:307px;top:1012px}
.client{left:329px;top:1022px;width:45px;height:39px;background:linear-gradient(180deg,#d9dfe4,#c4ccd3)}
.quote{left:382px;top:1017px;width:252px;font-size:8px;line-height:12.5px;color:#333}

/* footer */
.footer{left:0;top:1142px;width:682px;height:58px;background:var(--footer)}
.footer-links{left:60px;top:15px;font-size:7.5px;color:#fff;word-spacing:1px}
.footer-links span{margin:0 4px}
.copyright{left:62px;top:32px;font-size:7.5px;color:var(--blue)}
.footer .brand{left:450px;top:11px}
.footer .brand-name{color:#fff}
.footer .brand-dot{background:#fff}
</style>
</head>
<body>

<header>
  <a class="abs promo" href="#">
    <div class="abs promo-product" role="img" aria-label="Amber serum bottle with pump"></div>
    <div class="abs promo-product2" role="img" aria-label="Slim product tube"></div>
    <p class="abs promo-title">Transform Your Skin To A More<br>Youthful Appearance</p>
    <span class="abs promo-btn">Read More</span>
    <p class="abs promo-price">Peptide Renewal Serum<br><small>$12 (Save 52%)</small></p>
  </a>
  <div class="abs search">SEARCH...
    <svg width="11" height="11" viewBox="0 0 11 11"><circle cx="4.5" cy="4.5" r="3.5" fill="none" stroke="#999" stroke-width="1.3"/><path d="M7 7l3 3" stroke="#999" stroke-width="1.4"/></svg>
  </div>
  <div class="abs brand">
    <div class="brand-name">clearhaven<span>by Dermal &amp; Skin Clinic</span></div>
    <i class="brand-dot"></i>
  </div>
</header>

<nav class="abs nav">
  <a class="active" href="#">HOME</a><a href="#">ABOUT US</a><a href="#">TREATMENTS</a><a href="#">PRODUCTS</a><a href="#">RESULTS</a><a href="#">MEDIA</a><a href="#">SKIN CODITIONS</a>
</nav>

<section class="abs hero">
  <p class="abs hero-kicker sans-light">Come and Experience the</p>
  <h1 class="abs hero-title sans-light">NEW ARRIVALS<br>IN SKIN CARE</h1>
  <p class="abs hero-lede">Lorem ipsum dolor sit amet, consectetur adipiscing elit quis placerat .</p>
  <a class="abs btn btn-products" href="#">VIEW PRODUCTS</a>
  <a class="abs btn btn-more" href="#">READ MORE &gt;&gt;</a>
  <div class="abs hero-photo" role="img" aria-label="Woman with skin peeling back to reveal a clear complexion"></div>
</section>

<section>
  <article class="abs card" style="left:69px;width:178px">
    <div class="card-head">For Free Consultation</div>
    <p class="card-text" style="top:43px">Simply dummy text of the printing and types industry. Lorem Ipsum has industry.</p>
    <div class="field" style="top:75px">name</div>
    <div class="field" style="top:104px">address</div>
    <div class="field" style="top:132px;height:48px">tell us about your problem</div>
    <a class="card-btn book" href="#">BOOK ONLINE</a>
  </article>
  <article class="abs card" style="left:258px;width:176px">
    <div class="card-head"><i></i>Online Products</div>
    <div class="photo" role="img" aria-label="Woman splashing water on her face" style="background:linear-gradient(180deg,#cfe4ef,#b9d6e6 50%,#e6d0c3)"></div>
    <p class="card-text" style="top:143px">Our topical medications (creams, gels and ointments) are specially formulated to help you manage your skin condition.</p>
    <a class="card-btn" href="#">Purchase Products</a>
  </article>
  <article class="abs card" style="left:442px;width:176px">
    <div class="card-head"><i></i>Practitioners</div>
    <div class="photo" role="img" aria-label="Doctor examining a child with a stethoscope" style="background:linear-gradient(90deg,#e9eef2,#dcd3cc 50%,#d8c2b2)"></div>
    <p class="card-text" style="top:143px">Our topical medications (creams, gels and ointments) are specially formulated to help you manage your skin condition.</p>
    <a class="card-btn" href="#">Intranet Access</a>
  </article>
</section>

<section class="abs about-band">
  <p class="abs eyebrow" style="left:70px;top:16px">About</p>
  <h2 class="abs heading" style="left:70px;top:34px">Dr. Caspian Orlev</h2>
  <div class="abs doctor" role="img" aria-label="Smiling doctor in white coat holding a clipboard"></div>
  <p class="abs about-copy" style="top:74px">Simply dummy text of the printing and typesetting industry. Lorem Ipsum has been the industry's standard dummy text ever since the 1500s, when an unknown printer took a galley of type and scrambled it to make a type specimen book. It has survived not only five centuries.It was popularised in the 1960s with the release of Typeworth.</p>
  <ul class="abs bullets">
    <li>Donec vulputate et nisl a scelerisque .</li>
    <li>Nullam eros arcu, imperdiet eget magna sit amet.</li>
    <li>Curabitur metus nunc, varius eu velit et, lobortis .</li>
    <li>Morbi mi justo, interdum sit amet orci nec..</li>
    <li>Donec vulputate et nisl a scelerisque .</li>
    <li>Nullam eros arcu, imperdiet eget magna sit amet.</li>
  </ul>
  <div class="abs divider-v"></div>
  <p class="abs eyebrow" style="left:414px;top:20px">View</p>
  <h2 class="abs heading" style="left:414px;top:38px">Case Studies</h2>
  <svg class="abs arrows" width="14" height="9" viewBox="0 0 14 9"><path d="M5 1L2 4.5 5 8" fill="none" stroke="#999" stroke-width="1.3"/><path d="M9 1l3 3.5L9 8" fill="none" stroke="#222" stroke-width="1.6"/></svg>
  <div class="abs case" style="left:414px;background:linear-gradient(90deg,#c99a7d,#b9876a 49%,#dcc0a8 51%,#d2b197)" role="img" aria-label="Before and after wrinkle treatment"></div>
  <div class="abs case" style="left:520px;background:linear-gradient(90deg,#d59a90,#c9857b 49%,#e6cfc4 51%,#ddc2b5)" role="img" aria-label="Before and after acne treatment"></div>
  <p class="abs viewall" style="left:581px;top:161px">View All</p>
  <p class="abs case-copy">Simply dummy text of the printing and typesetting industry. Lorem Ipsum has been the industry's standard dummy text ever since the 1500s, when an unknown printer took a galley of type and scrambled.</p>
</section>

<section>
  <p class="abs eyebrow" style="left:65px;top:966px">What's Unique</p>
  <h2 class="abs heading" style="left:65px;top:985px">About Our Treatment Protcols</h2>
  <span class="abs step step-1" style="top:1015px">1</span>
  <p class="abs step-text" style="top:1014px">Simply dummy text of the printing and typesetting industry. Lorem Ipsum has been the industry's</p>
  <div class="abs divider-h"></div>
  <span class="abs step step-2" style="top:1059px">2</span>
  <p class="abs step-text" style="top:1057px">Dummy text of the printing and typesetting industry. Lorem Ipsum has been the industry's</p>
  <p class="abs viewall" style="left:68px;top:1092px">View All</p>

  <p class="abs eyebrow" style="left:318px;top:964px">Client's</p>
  <h2 class="abs heading" style="left:318px;top:983px">Testimonial</h2>
  <svg class="abs brace" width="16" height="60" viewBox="0 0 16 60"><path d="M14 1C6 1 8 12 7 22 6 27 4 29 1 30 4 31 6 33 7 38 8 48 6 59 14 59" fill="none" stroke="#ddd" stroke-width="2.5"/></svg>
  <div class="abs client" role="img" aria-label="Client portrait"></div>
  <p class="abs quote">Simply dummy text of the printing and typesetting industry. Lorem Ipsum has been the industry's standard dummy text ever since the 1500s, when an unknown printer took a galley of type and scrambled it to make a type specimen book. It has survived not only five centuries.It was popularised in the 1960s with the release of Typeworth.</p>
  <p class="abs viewall" style="left:329px;top:1092px">View All</p>
</section>

<footer class="abs footer">
  <p class="abs footer-links">Home<span>|</span>About Us<span>|</span>Treatments<span>|</span>Our services<span>|</span>Our Products</p>
  <p class="abs copyright">© 2015 Clearhaven. All rights reserved.</p>
  <div class="abs brand">
    <div class="brand-name">clearhaven<span>by Dermal &amp; Skin Clinic</span></div>
    <i class="brand-dot"></i>
  </div>
</footer>

</body>
</html>
```